Poster design for The Dorrable Co.

Create a poster that will sell our company, all the information needed is on our website @ thedorrableco.co.uk
Creative design is down to you.

I have attached the AI for our logo.

```html
<!DOCTYPE html>
<html lang="en">
<head>
<meta charset="utf-8">
<title>The Dorrable Co. – Poster</title>
<link rel="stylesheet" href="https://fonts.googleapis.com/css2?family=EB+Garamond:ital,wght@0,400;0,500;1,600;1,700&family=Pinyon+Script&display=swap">
<style>
  :root {
    --frame: #0c0c0c;
    --paper: #dcdcd5;
    --ink: #2b2a24;
    --rule: #2e2d28;
    --brand-red: #9e2a2b;
    --muted: #7a7a74;
    --hero-dark: #55574b;
    --hero-light: #cfcdc2;
    --panel-white: #f3f2ee;
  }
  * { margin: 0; padding: 0; box-sizing: border-box; }
  html, body { width: 849px; height: 1200px; overflow: hidden; background: var(--frame); }
  .poster {
    position: relative;
    width: 849px;
    height: 1200px;
    background: var(--frame);
  }
  .poster__panel {
    position: absolute;
    left: 13px; top: 13px; right: 13px; bottom: 12px;
    background: var(--paper);
  }
  .headline {
    position: absolute;
    left: 0; right: 0; top: 0; height: 99px;
    display: flex; align-items: center; justify-content: center;
    font-family: "Pinyon Script", cursive;
    font-weight: 400;
    font-size: 58px;
    color: var(--ink);
    letter-spacing: 1px;
    padding-top: 4px;
  }
  .hero {
    position: absolute;
    left: 0; right: 0; top: 99px; height: 625px;
    background: linear-gradient(180deg, var(--hero-dark) 0%, var(--hero-light) 100%);
  }
  .hero__badge {
    position: absolute;
    left: 528px; top: 512px;
    width: 255px; height: 74px;
    background: var(--panel-white);
    display: flex; flex-direction: column; align-items: center; justify-content: center;
    font-family: "EB Garamond", serif;
  }
  .hero__badge-name { font-size: 24px; font-weight: 500; color: var(--brand-red); line-height: 1; }
  .hero__badge-tag { font-size: 9px; letter-spacing: 1.5px; color: var(--muted); margin-top: 4px; }
  .services {
    position: absolute;
    left: 0; right: 0; top: 745px;
  }
  .services__heading {
    display: flex; align-items: center; gap: 22px;
    font-family: "EB Garamond", serif;
    font-style: italic; font-weight: 700;
    font-size: 30px; color: var(--ink);
  }
  .services__heading::before,
  .services__heading::after {
    content: ""; flex: 1; height: 1.5px; background: var(--rule);
  }
  .services__list {
    position: absolute;
    top: 64px;
    list-style: none;
    font-family: "EB Garamond", serif;
    font-size: 31px; line-height: 42.5px; color: var(--ink);
  }
  .services__list--left { left: 85px; }
  .services__list--right { left: 368px; }
  .divider {
    position: absolute;
    left: 0; right: 0; top: 1004px;
    display: block;
  }
  .signoff {
    position: absolute;
    left: 0; right: 0; top: 1112px;
    text-align: center;
    font-family: "EB Garamond", serif;
  }
  .signoff__name { font-size: 32px; font-weight: 500; color: var(--brand-red); line-height: 1; }
  .signoff__tag { font-size: 10px; letter-spacing: 1.5px; color: var(--muted); margin-top: 4px; }
</style>
</head>
<body>
<main class="poster">
  <div class="poster__panel">
    <h1 class="headline">“Simple, Smart &amp; Beautiful”</h1>

    <div class="hero" role="img" aria-label="Sepia-toned beach landscape photograph with a wide cloudy sky, calm bay and white sand">
      <div class="hero__badge">
        <div class="hero__badge-name">The Dorrable Co.</div>
        <div class="hero__badge-tag">PHOTOGRAPHY</div>
      </div>
    </div>

    <section class="services">
      <h2 class="services__heading">Services &amp; Products</h2>
      <ul class="services__list services__list--left">
        <li>Website Design</li>
        <li>Logo Design</li>
        <li>Domain Names</li>
      </ul>
      <ul class="services__list services__list--right">
        <li>Website Hosting</li>
        <li>Domain Linked Email Accounts</li>
        <li>Website Management</li>
        <li>Photography Graphic Stock</li>
      </ul>
    </section>

    <svg class="divider" width="823" height="34" viewBox="0 0 823 34" aria-hidden="true">
      <line x1="0" y1="17" x2="392" y2="17" stroke="var(--rule)" stroke-width="1.5"/>
      <circle cx="412" cy="17" r="15" fill="none" stroke="var(--rule)" stroke-width="1.5"/>
      <line x1="432" y1="17" x2="823" y2="17" stroke="var(--rule)" stroke-width="1.5"/>
    </svg>

    <footer class="signoff">
      <div class="signoff__name">The Dorrable Co.</div>
      <div class="signoff__tag">SIMPLE, SMART AND BEAUTIFUL</div>
    </footer>
  </div>
</main>
</body>
</html>
```